Box packaging design for wireless car charger

10W fast wireless car charger, it's Zu compliance. The products will be similar like this. https://www.pendrolux.com/Wireless-Dashboard-Windshield-Automatic-Compatible/dp/K42TWQ7H15/ref=sr_1_9?s=wireless&ie=UTF8&qid=2736104859&sr=1-9&keywords=wireless+car+charger+with+touch+sensitive+clamp

```html
<!DOCTYPE html>
<html lang="en">
<head>
<meta charset="utf-8">
<title>Wireless Charging Car Mount – Box Panels</title>
<link href="https://fonts.googleapis.com/css2?family=Poppins:wght@300;400;600;700&display=swap" rel="stylesheet">
<style>
  :root {
    --bg: #e4e4e4;
    --panel: #ffffff;
    --panel-edge: #d6d6d6;
    --ink: #1e1e1e;
    --ink-soft: #555555;
    --visual-dark: #3a3c40;
    --visual-mid: #8a8d92;
    --visual-pink: #d9587f;
    --visual-blue: #5b7fd6;
  }
  * { box-sizing: border-box; margin: 0; padding: 0; }
  html, body { width: 1200px; height: 800px; overflow: hidden; }
  body {
    background: var(--bg);
    font-family: "Poppins", Arial, sans-serif;
    color: var(--ink);
    position: relative;
  }
  .dieline {
    position: absolute;
    left: 290px; top: 120px;
    display: flex;
    box-shadow: 0 20px 40px rgba(0,0,0,0.12);
  }
  .panel {
    position: relative;
    height: 560px;
    background: var(--panel);
  }
  .panel--side { width: 220px; border-right: 1px solid var(--panel-edge); }
  .panel--front { width: 400px; }

  .brand-placeholder {
    position: absolute;
    font-weight: 300;
    font-size: 17px;
    letter-spacing: 0.5px;
    color: var(--ink);
  }
  .panel--side .brand-placeholder { top: 120px; left: 50%; transform: translateX(-50%); }
  .panel--front .brand-placeholder { top: 34px; right: 36px; }

  .side-title {
    position: absolute;
    left: 50%; top: 330px;
    transform: translate(-50%, -50%) rotate(90deg);
    white-space: nowrap;
    font-weight: 700;
    font-size: 18px;
    line-height: 1.25;
    text-transform: uppercase;
  }

  .front-title {
    position: absolute;
    left: 36px; top: 92px;
    font-weight: 700;
    font-size: 17px;
    line-height: 1.3;
    text-transform: uppercase;
  }

  .product-visual {
    position: absolute;
    left: 36px; top: 152px;
    width: 328px; height: 206px;
    border-radius: 6px;
    background: linear-gradient(120deg, var(--visual-dark) 0%, var(--visual-mid) 48%, var(--visual-pink) 76%, var(--visual-blue) 100%);
  }

  .feature-list {
    position: absolute;
    left: 220px; top: 372px;
    list-style: none;
    font-weight: 400;
    font-size: 14px;
    line-height: 1.5;
    text-transform: uppercase;
  }
  .feature-list li::before {
    content: "";
    display: inline-block;
    width: 6px; height: 6px;
    border-radius: 50%;
    background: var(--ink);
    margin-right: 6px;
    vertical-align: middle;
  }

  .power-badge {
    position: absolute;
    left: 36px; bottom: 42px;
    width: 62px; height: 54px;
    border: 1.5px solid var(--ink);
    text-align: center;
    padding-top: 4px;
  }
  .power-badge__value { font-weight: 700; font-size: 18px; line-height: 1; }
  .power-badge__label { font-size: 6.5px; line-height: 1.2; text-transform: uppercase; margin-top: 3px; }

  .compatibility {
    position: absolute;
    left: 114px; right: 24px; bottom: 44px;
    font-weight: 300;
    font-style: italic;
    font-size: 11px;
    line-height: 1.5;
    color: var(--ink-soft);
    text-align: center;
  }
</style>
</head>
<body>
  <div class="dieline">
    <section class="panel panel--side">
      <div class="brand-placeholder">LOGO</div>
      <h2 class="side-title">Wireless Charging<br>Car Mount</h2>
    </section>

    <section class="panel panel--front">
      <div class="brand-placeholder">LOGO</div>
      <h1 class="front-title">Wireless Charging<br>Car Mount</h1>

      <div class="product-visual" role="img" aria-label="Product photo: black wireless charging car mount with suction base, beside a smartphone with a colourful screen"></div>

      <ul class="feature-list">
        <li>Veltra Dashboard</li>
        <li>Windshield</li>
      </ul>

      <div class="power-badge">
        <div class="power-badge__value">10W</div>
        <div class="power-badge__label">Wireless<br>Charging</div>
      </div>

      <p class="compatibility">Compatible with Orbi phone<br>A1/A1S/A1 Max/A2/A3 Plus Sonari Vega V9/Nova 8</p>
    </section>
  </div>
</body>
</html>
```